Security and Automation Company based in Texas and needs logo design also

Looking for a new logo design for our company - we are based in Texas and specialize in camera, security and home automation - We do want the main company name(Brightline Guard and Controls of Texas) with our parent company in small letters below (a Veloran Partners, LLC Company) and our License number needs to be included in the design - K74836 - Darker shades of blue preferred

Target Market(s)

We work with everyone from home to large corporate - so clean design would be helpful

Industry/Entity Type

It Company

Contact Information for Business Card

PO Box 4719
Cedar Hollow, Texas 75961
Leave a spot for the phone number and email address

Logo Text

Brightline Guard and Controls of Texas/a Veloran Partners Company/K74836

Font styles to use
Sans Serif

Colors
0255a3

```html
<!DOCTYPE html>
<html lang="en">
<head>
<meta charset="utf-8">
<title>Brightline Guard and Controls of Texas – Business Card</title>
<link href="https://fonts.googleapis.com/css2?family=Josefin+Sans:wght@400;600&display=swap" rel="stylesheet">
<style>
  :root{
    --bg:#ececec;
    --card:#ffffff;
    --blue:#2f63ad;
    --blue-deep:#1d5aa6;
    --blue-soft:#5d88c4;
    --rule:#c4d5ec;
    --ink:#2a2a2a;
    --mark-ink:#262a33;
  }
  *{margin:0;padding:0;box-sizing:border-box}
  html,body{width:1200px;height:783px;overflow:hidden;background:var(--bg)}
  body{position:relative;font-family:"Josefin Sans",sans-serif;color:var(--ink)}
  .card{position:absolute;top:237px;width:540px;height:309px;box-shadow:0 14px 30px rgba(0,0,0,.18)}
  .card-front{left:40px;background:var(--card);overflow:hidden}
  .card-back{left:620px;background:linear-gradient(90deg,var(--blue-deep),#4a7bb9);display:flex;align-items:center;justify-content:center;gap:12px}
  .brand-mark{position:absolute;left:40px;top:100px;display:flex;align-items:center;gap:10px}
  .brand-dot{width:22px;height:22px;border-radius:50%;background:var(--blue)}
  .brand-name{font-size:20px;font-weight:600;color:var(--blue);letter-spacing:.5px}
  .company{position:absolute;left:222px;top:46px;width:260px}
  .company-name{font-size:19px;line-height:20px;color:var(--blue);text-transform:uppercase;letter-spacing:.6px}
  .company-parent{margin-top:10px;font-size:8.5px;color:var(--blue);text-transform:uppercase;letter-spacing:.8px}
  .rules{position:absolute;inset:0}
  .contact{position:absolute;left:228px;top:190px;font-size:10px;line-height:14px;text-transform:uppercase}
  .contact .spaced{letter-spacing:3px}
  .license{position:absolute;left:432px;top:102px;text-transform:uppercase}
  .license-label{font-size:8px;letter-spacing:3px;line-height:10px}
  .license-number{margin-top:4px;display:inline-block;background:var(--blue-soft);color:#fff;font-size:15px;padding:4px 20px 1px 6px;letter-spacing:1px}
  .web{position:absolute;left:428px;top:252px;font-size:7px;line-height:11px;text-transform:uppercase;color:#555;letter-spacing:.6px}
  .web span{color:var(--blue);margin-right:4px}
  .person{position:absolute;left:22px;top:240px;color:#fff;text-transform:uppercase}
  .person-name{font-size:20px;letter-spacing:1.5px}
  .person-role{font-size:8.5px;letter-spacing:1px;margin-top:2px}
  .back-dot{width:26px;height:26px;border-radius:50%;background:var(--mark-ink)}
  .back-name{font-size:24px;font-weight:600;color:var(--mark-ink);letter-spacing:.5px}
</style>
</head>
<body>
  <section class="card card-front" aria-label="Business card front">
    <svg class="rules" width="540" height="309" viewBox="0 0 540 309" aria-hidden="true">
      <polygon points="0,228 205,228 190,309 0,309" fill="#2f63ad"/>
      <polygon points="150,228 205,228 240,255 190,309" fill="#4d7bbd"/>
      <polygon points="150,228 205,228 240,255" fill="#6f96cc"/>
      <line x1="190" y1="300" x2="540" y2="300" stroke="#c4d5ec" stroke-width="1"/>
      <line x1="240" y1="255" x2="540" y2="255" stroke="#c4d5ec" stroke-width="1"/>
      <line x1="200" y1="170" x2="540" y2="170" stroke="#c4d5ec" stroke-width="1"/>
      <line x1="420" y1="88" x2="420" y2="170" stroke="#c4d5ec" stroke-width="1"/>
      <line x1="420" y1="88" x2="540" y2="88" stroke="#c4d5ec" stroke-width="1"/>
    </svg>

    <div class="brand-mark">
      <span class="brand-dot"></span>
      <span class="brand-name">BGC Texas</span>
    </div>

    <div class="company">
      <p class="company-name">Brightline Guard<br>and Controls<br>of Texas</p>
      <p class="company-parent">a Veloran Partners, LLC Company</p>
    </div>

    <div class="license">
      <p class="license-label">License<br>Number</p>
      <p class="license-number">K74836</p>
    </div>

    <div class="contact">
      <p class="spaced">PO Box 4719</p>
      <p class="spaced">+000-555-010-010</p>
      <p>Cedar Hollow, Texas 75961</p>
    </div>

    <div class="web">
      <p><span>@</span>www.website.com</p>
      <p><span>✉</span>email@mailbox.com</p>
    </div>

    <div class="person">
      <p class="person-name">Full Name</p>
      <p class="person-role">General Manager</p>
    </div>
  </section>

  <section class="card card-back" aria-label="Business card back">
    <span class="back-dot"></span>
    <span class="back-name">BGC Texas</span>
  </section>
</body>
</html>
```